Black Car Limousine transportation business in Naples Florida

Brightway stand for my reliability and DPR stands for Devotion, P and R are the first initials of my children's names. It should show professionalism and a dedication to customer service. We keep our clients identities private. Show our professionalism. We are Black car Black tie company. We service transportation on a reserve basis to and from residents, airports, casinos, hotels,

Target Market(s)

It is a Private car service. High end clients. Businesses, Celebrity and athletes. Service to airports, hotels, special events.

Industry/Entity Type

Business

Contact Information for Business Card

A pearl metallic or Luster card. Standard business card size. Would like the name, Company email, show we take credit cards and phone number. Currently I don't have a website but will like to add later.

Logo Text

BRIGHTWAY DPR TRANSPORTATION

Font styles to use
Serif

Colors
eaeaea
000000

Requirements
Must have
• Must have Company email, show we take credit cards and phone number. Currently I don't have a website but will like to add later.
Nice to have
• Would like to stay with a black and white theme. Open to some color trim.
Should not have
• Open to suggestions

```html
<!DOCTYPE html>
<html lang="en">
<head>
<meta charset="utf-8">
<title>Brightway DPR Transportation – Business Card</title>
<link rel="stylesheet" href="https://fonts.googleapis.com/css2?family=Cinzel:wght@400;500&display=swap">
<style>
  :root {
    --page: #ffffff;
    --black: #000000;
    --black-soft: #1a1a1a;
    --black-sheen: #3a3a3a;
    --pearl: #eaeaea;
    --pearl-light: #f7f7f7;
    --pearl-shade: #d2d2d2;
    --silver-light: #f4f4f4;
    --silver-mid: #bdbdbd;
    --silver-dark: #8c8c8c;
    --trim-red: #a3081a;
    --ink-light: #eaeaea;
    --ink-soft: #cfcfcf;
    --ink-dark: #000000;
    --ink-muted: #3c3c3c;
    --vehicle-dark: #0b0b0d;
    --vehicle-mid: #4a4a4e;
  }
  * { margin: 0; padding: 0; box-sizing: border-box; }
  html, body {
    width: 1112px; height: 1200px; overflow: hidden;
    background: var(--page);
  }
  body {
    position: relative;
    font-family: "Cinzel", "Times New Roman", serif;
    color: var(--ink-light);
  }
  .card {
    position: absolute;
    width: 862px; height: 505px;
    overflow: hidden;
  }
  .card--front { left: 52px; top: 51px; }
  .card--back { left: 142px; top: 587px; }

  .card__metal {
    position: absolute; left: 0; top: 0; width: 100%; height: 335px;
    background:
      linear-gradient(180deg, rgba(255,255,255,0.04) 0%, rgba(255,255,255,0.08) 45%, rgba(0,0,0,0.35) 100%),
      linear-gradient(90deg, var(--black) 0%, var(--black-soft) 18%, var(--black-sheen) 38%, var(--black-soft) 52%, var(--black-sheen) 66%, var(--black) 84%, var(--black-soft) 100%);
  }
  .card__trim {
    position: absolute; left: 0; top: 335px; width: 100%; height: 22px;
    background: linear-gradient(180deg, var(--silver-light) 0%, var(--silver-mid) 55%, var(--silver-dark) 100%);
    border-top: 3px solid var(--trim-red);
  }
  .card__pearl {
    position: absolute; left: 0; top: 357px; width: 100%; height: 148px;
    background: linear-gradient(180deg, var(--pearl-light) 0%, var(--pearl) 55%, var(--pearl-shade) 100%);
  }

  .brand {
    position: absolute; left: 40px; top: 42px;
    letter-spacing: 2px;
    line-height: 1;
    color: var(--ink-light);
  }
  .brand__name { font-size: 34px; display: block; }
  .brand__initials { font-size: 50px; font-weight: 500; }
  .brand__tagline { font-size: 28px; display: block; margin-top: 16px; color: var(--ink-soft); }

  .holder {
    position: absolute; right: 48px; top: 312px;
    transform: translateY(-100%);
    font-size: 30px; letter-spacing: 1.5px;
    color: var(--ink-soft);
  }

  .contact {
    position: absolute; right: 46px;
    display: flex; align-items: center; gap: 14px;
    color: var(--ink-dark);
    white-space: nowrap;
  }
  .contact--phone { top: 388px; font-size: 38px; letter-spacing: 2px; }
  .contact--email { top: 462px; font-size: 16px; letter-spacing: 0.5px; }
  .contact__icon { flex: none; fill: none; stroke: var(--ink-dark); stroke-width: 2; }
  .contact__icon--phone { fill: var(--ink-dark); stroke: none; }

  .payment {
    position: absolute; left: 40px; top: 394px;
    display: flex; flex-direction: column; gap: 10px;
    color: var(--ink-muted);
  }
  .payment__cards { display: flex; gap: 10px; }
  .payment__card { fill: none; stroke: var(--ink-dark); stroke-width: 2; }
  .payment__stripe { fill: var(--ink-dark); }
  .payment__label { font-size: 13px; letter-spacing: 1px; }

  .vehicle {
    position: absolute; left: 137px; top: 65px; width: 621px; height: 270px;
    border-radius: 60px 90px 0 0;
    background: radial-gradient(ellipse at 50% 40%, var(--vehicle-mid) 0%, var(--vehicle-dark) 75%);
  }

  .wordmark {
    position: absolute; left: 0; width: 100%; top: 432px;
    transform: translateY(-50%);
    text-align: center;
    letter-spacing: 2px; line-height: 1;
    color: var(--ink-dark);
    white-space: nowrap;
  }
  .wordmark__word { font-size: 28px; }
  .wordmark__initials { font-size: 44px; font-weight: 500; }
</style>
</head>
<body>

  <section class="card card--front">
    <div class="card__metal"></div>
    <div class="card__trim"></div>
    <div class="card__pearl"></div>

    <div class="brand">
      <span class="brand__name">Brightway <span class="brand__initials">DPR</span></span>
      <span class="brand__tagline">Transportation</span>
    </div>

    <div class="holder">Daniel Marchetti</div>

    <div class="payment">
      <div class="payment__cards" aria-hidden="true">
        <svg width="40" height="28" viewBox="0 0 40 28"><rect class="payment__card" x="1" y="1" width="38" height="26" rx="4"/><rect class="payment__stripe" x="1" y="7" width="38" height="5"/></svg>
        <svg width="40" height="28" viewBox="0 0 40 28"><rect class="payment__card" x="1" y="1" width="38" height="26" rx="4"/><rect class="payment__stripe" x="1" y="7" width="38" height="5"/></svg>
        <svg width="40" height="28" viewBox="0 0 40 28"><rect class="payment__card" x="1" y="1" width="38" height="26" rx="4"/><rect class="payment__stripe" x="1" y="7" width="38" height="5"/></svg>
      </div>
      <span class="payment__label">Credit Cards Accepted</span>
    </div>

    <div class="contact contact--phone">
      <svg class="contact__icon contact__icon--phone" width="22" height="32" viewBox="0 0 22 32" aria-hidden="true">
        <path d="M6 1 L10 1 L11 9 L7 11 C7 16 9 21 12 24 L16 21 L21 27 L18 31 C10 30 2 20 2 8 Z"/>
      </svg>
      <span>555.210.4477</span>
    </div>

    <div class="contact contact--email">
      <svg class="contact__icon" width="26" height="20" viewBox="0 0 28 22" aria-hidden="true">
        <path d="M2 9 L14 2 L26 9 L26 20 L2 20 Z M2 9 L14 15 L26 9"/>
      </svg>
      <span>brightwayDPRtransportation@mailbox.com</span>
    </div>
  </section>

  <section class="card card--back">
    <div class="card__metal"></div>
    <div class="vehicle" role="img" aria-label="Black luxury SUV shown from the front three-quarter view"></div>
    <div class="card__trim"></div>
    <div class="card__pearl"></div>

    <div class="wordmark">
      <span class="wordmark__word">Brightway</span>
      <span class="wordmark__initials">DPR</span>
      <span class="wordmark__word">Transportation</span>
    </div>
  </section>

</body>
</html>
```